we are a mobile auto windscreen replacement business we are looking for a smart, stylish designed card on a matte black base color with large metallic silver KVT (similar to the zenpod box)
over the whole face of the card but down the bottom have (your local automotive & machinery glass specialist) & over the back

Reason: I'm looking for a design like no other something that really wows people to grab a card & use my business

Target Market(s)

Adults in western countries that own an automotive fleet company or anybody that owns a car

Industry/Entity Type

Automotive

Contact Information for Business Card

front: KVTglassworks
Back: MORRIS 0482 65 71 93 Abn: 52840193657
morris@kvtglassworks.com.au & www.kvtglassworks.com.au

Logo styles of interest
Lettermark Logo
Requirements
Must have
• Metallic font on matte background
Nice to have
• 3D font that's glass or the word KVT smashed into glass on a black background I've added some pictures that maybe you could incorporate in the background or font it would be great to see a professionals ideas

```html
<!DOCTYPE html>
<html lang="en">
<head>
<meta charset="utf-8">
<title>KVT Glassworks – Business Card</title>
<link href="https://fonts.googleapis.com/css2?family=Marcellus&family=Tenor+Sans&display=swap" rel="stylesheet">
<style>
  :root {
    --page: #f2f2f0;
    --card-black: #0b0a0a;
    --silver: #d4d6d8;
    --text-light: #e8e8e8;
    --text-soft: #cfcfcf;
    --photo-top: #5c5c66;
    --photo-mid: #2a2a2e;
    --photo-low: #0a0a0c;
  }
  * { margin: 0; padding: 0; box-sizing: border-box; }
  html, body {
    width: 1200px; height: 1000px; overflow: hidden;
    background: var(--page);
  }
  .canvas { position: relative; width: 1200px; height: 1000px; }
  .card {
    position: absolute;
    width: 594px; height: 368px;
    background: var(--card-black);
    overflow: hidden;
  }
  .card--front { left: 322px; top: 70px; }
  .card--back  { left: 322px; top: 522px; }

  .front-photo {
    position: absolute; inset: 0;
    background:
      radial-gradient(ellipse 60% 45% at 50% 35%, var(--photo-top) 0%, var(--photo-mid) 45%, transparent 80%),
      linear-gradient(180deg, #1c1c20 0%, #3a3a44 55%, var(--photo-low) 60%, #000 100%);
  }
  .wordmark {
    position: absolute;
    font-family: "Tenor Sans", sans-serif;
    color: var(--silver);
    line-height: 1;
    letter-spacing: 2px;
  }
  .card--front .wordmark {
    left: 0; right: 0; top: 160px;
    text-align: center; font-size: 60px;
  }
  .tagline {
    font-family: "Tenor Sans", sans-serif;
    font-variant: small-caps;
    color: var(--text-light);
    letter-spacing: 1.5px;
  }
  .card--front .tagline {
    position: absolute; left: 0; right: 0; top: 218px;
    text-align: center; font-size: 15px;
  }
  .card--back .wordmark { left: 52px; top: 94px; font-size: 74px; }
  .card--back .tagline {
    position: absolute; left: 320px; top: 120px;
    font-size: 16px; line-height: 19px; letter-spacing: 2px;
  }
  .contact {
    position: absolute; left: 320px; top: 246px;
    font-family: "Marcellus", serif;
    color: var(--text-soft);
    font-size: 16px; line-height: 24px;
  }
  .contact .name { color: var(--text-light); font-size: 18px; margin-right: 10px; }
  .contact .phone { font-size: 17px; }
</style>
</head>
<body>
<main class="canvas">
  <section class="card card--front">
    <div class="front-photo" role="img" aria-label="Dark studio photograph of a modern sports car seen head-on with glowing headlights"></div>
    <div class="wordmark">KVT</div>
    <p class="tagline">Your Local Automotive &amp; Machinery Glass Specialist</p>
  </section>

  <section class="card card--back">
    <div class="wordmark">KVT</div>
    <p class="tagline">Your Local Automotive &amp;<br>Machinery Glass Specialist</p>
    <div class="contact">
      <p><span class="name">MORRIS</span><span class="phone">0482 65 71 93</span></p>
      <p>Abn: 52840193657</p>
      <p>morris@kvtglassworks.com.au</p>
      <p>www.kvtglassworks.com.au</p>
    </div>
  </section>
</main>
</body>
</html>
```